FALKENHOF KONTOR KAFFEECATERING AUF MESSEN & EVENTS
Wir bieten ein hochwertiges Barista Catering inklusive komplettem Messe-Full- service an. Unser professionell geschultes Barista-Team sorgt für optimalen Kaffeege- nuss auf Messen, Kongressen und Events aller Art. Der elegante Abschluss mit einem Muster auf der Tasse, genannt „Latte Art“ , ist das Highlight unserer Dienstleistung.
Ob fest integriert im Messestand, als mobi- le Espressobar mit eigener Theke oder als Coffeebike- wir haben für jeden Anlass die passende Variante.
Branden Sie unser Equipment mit Ihrem Firmenlogo! Gerne beraten wir Sie hierzu.
HOSTESSENAGENTUR
Wählen Sie aus über 8.000 Hostessen und und mehr als 20 Sprachen! Unsere Hostes- sen und Hosts begleiten Sie auf:
• Messen
• Kongresse
• VIP-Veranstaltungen • Promotion
• Events aller Art
COCKTAIlS & SMOOTHIES MIT FIRMENlOGO
Unser mobiler Cocktailservice eignet sich für jede Art von Veranstaltung und ist eine geniale Ergänzung zu jedem Messestand.
Erweitern Sie das bestehende Cocktailan- gebot mit gebrandeten Smoothies in fünf verschiedenen Geschmacksrichtungen.
MESSECATERING
Egal ob klassische Häppchen, trendiges Finger- food oder Menüs in allen Variationen - sprechen Sie uns an!
Kurzum, unser Schwerpunkt liegt auf Barista-und Personalservice. An 3 Standorten-München, Berlin, Frankfurt.
Wir möchten gerne einen monatlichen Newsletter raussenden, den wir mittel MailChimp selber pflegen können. Nur brauchen wir eben dazu ein Design/Template was veränderbar ist.
Wir freuen uns auf tolle Designs!

```html
<!DOCTYPE html>
<html lang="de">
<head>
<meta charset="utf-8">
<title>Falkenhof Kontor – Newsletter</title>
<link rel="stylesheet" href="https://fonts.googleapis.com/css2?family=Crimson+Text:wght@400;600;700&family=Raleway:wght@400;600;700&display=swap">
<style>
:root{
  --bg-top:#2b1710;
  --bg-bottom:#1a0d08;
  --brown:#8b5a3c;
  --brown-dark:#7a4e33;
  --ink:#1d1d1d;
  --text:#2b2b2b;
  --muted:#9a9a9a;
  --paper:#ffffff;
  --cream:#f4ece5;
  --night:#0e0d0d;
  --footer:#262323;
  --footer-text:#d8d2cc;
}
*{margin:0;padding:0;box-sizing:border-box}
html,body{width:1200px;height:5350px;overflow:hidden}
body{
  background:linear-gradient(180deg,var(--bg-top),var(--bg-bottom));
  font-family:"Raleway",sans-serif;color:var(--text);
  position:relative;
}
.mail{position:absolute;left:240px;top:73px;width:720px}
.photo{width:100%;display:block}
.serif{font-family:"Crimson Text",serif}
.block{background:var(--paper);text-align:center;position:relative}
.heading{font-family:"Crimson Text",serif;font-weight:400;color:var(--brown);font-size:52px;line-height:1.25;letter-spacing:.5px}
.divider{width:68px;height:5px;background:var(--muted);margin:0 auto}
.copy{font-size:17.5px;line-height:29px;color:var(--text)}
.button{display:inline-block;background:var(--brown);color:#fff;font-family:"Crimson Text",serif;font-weight:700;font-size:22px;line-height:58px;height:58px;padding:0 32px;text-decoration:none;letter-spacing:.3px}

/* intro */
.intro{height:702px;padding-top:48px}
.brand{display:flex;align-items:center;justify-content:center;gap:14px;height:166px}
.brand-dot{width:18px;height:18px;background:var(--brown);border-radius:50%}
.brand-name{font-family:"Crimson Text",serif;font-weight:700;font-size:50px;color:var(--ink);letter-spacing:1px}
.cities{font-family:"Crimson Text",serif;font-size:28px;color:var(--ink);margin-top:6px;letter-spacing:.5px}
.intro-copy{font-size:15px;line-height:29px;color:var(--text);width:590px;margin:30px auto 0}
.intro-copy p+p{margin-top:28px}

/* hostessen */
.hostessen{height:511px;padding-top:24px}
.hostessen .divider{margin-top:20px}
.hostessen .copy{margin-top:30px}
.services{list-style:none;font-weight:700;font-size:21px;line-height:35px;color:var(--ink);margin-top:20px}
.hostessen .button{margin-top:48px;position:relative;z-index:2}
.cup{position:absolute;right:0;bottom:0;width:180px;height:200px;background:radial-gradient(ellipse at 60% 55%,#3a2418 0%,#9c8a7c 45%,rgba(255,255,255,0) 72%)}

/* cocktails */
.cocktails{background:var(--night);height:504px;padding-top:42px;text-align:center;position:relative}
.cocktails .heading{line-height:66px}
.cocktails .divider{margin-top:22px;background:#555}
.cocktails .copy{color:#eee;margin-top:28px}
.cocktails .button{margin-top:52px}
.leaf{position:absolute;border-radius:50%;background:radial-gradient(circle at 40% 40%,#7fd04a,#2f8f1e 70%,rgba(47,143,30,0) 72%)}
.leaf-left{left:-10px;top:350px;width:190px;height:190px;z-index:3}

/* messe */
.messe{height:428px;padding-top:105px}
.messe .divider{margin-top:14px}
.messe .copy{margin-top:28px}
.messe .button{margin-top:40px}

/* news */
.news-head{height:185px;padding-top:52px}
.news-head .divider{margin-top:14px}
.news-grid{display:grid;grid-template-columns:1fr 1fr}
.card{text-align:center;background:var(--paper)}
.card.tint{background:var(--cream)}
.card-photo{height:251px}
.card-body{height:336px;padding-top:26px}
.card-title{font-family:"Crimson Text",serif;color:var(--brown);font-size:38px;line-height:1.2}
.card .divider{width:76px;height:4px;margin-top:14px}
.card-copy{font-size:15px;line-height:24px;width:300px;margin:30px auto 0;color:var(--text)}
.card .button{margin-top:38px;font-size:21px;line-height:54px;height:54px;padding:0 34px}

/* footer */
.footer{background:var(--footer);height:661px;color:var(--footer-text);padding:0 36px;position:relative}
.footer-brand{display:flex;align-items:center;gap:26px;padding-top:104px}
.footer-rule{flex:1;height:1px;background:#8a8580}
.footer-brand .brand-name{color:var(--footer-text);font-size:40px}
.footer-brand .brand-dot{background:var(--footer-text);width:14px;height:14px}
.addresses{display:flex;justify-content:space-between;margin-top:86px;font-size:13.5px;line-height:25px}
.addresses strong{font-size:16px;font-weight:700;color:#eee;display:block;line-height:24px}
.unsubscribe{text-align:center;font-size:13.5px;line-height:30px;margin-top:62px}
.unsubscribe a{color:inherit}
.footer-line{height:1px;background:#4a4645;margin-top:46px}
.footer-bottom{display:flex;justify-content:space-between;align-items:center;margin-top:30px;font-size:14px}
.footer-bottom strong{color:#eee}
.social{display:flex;gap:14px}
.social span{width:36px;height:36px;border-radius:50%;background:var(--footer-text);display:block}
.leaf-bottom{left:940px;top:5010px;width:180px;height:170px}
</style>
</head>
<body>
<main class="mail">
  <div class="photo" style="height:253px;background:linear-gradient(180deg,#d9cfc9,#b79a86 55%,#e8e3df)" role="img" aria-label="Barista gießt Milchschaum mit Latte Art in eine Tasse"></div>

  <section class="block intro">
    <div class="brand"><span class="brand-dot"></span><span class="brand-name">FALKENHOF KONTOR</span></div>
    <p class="cities">München - Berlin - Frankfurt</p>
    <div class="intro-copy">
      <p>Wir bieten ein hochwertiges Barista Catering inklusive komplettem Messe-Full- service an. Unser professionell geschultes Barista-Team sorgt für optimalen Kaffeege- nuss auf Messen, Kongressen und Events aller Art. Der elegante Abschluss mit einem Muster auf der Tasse, genannt „Latte Art“ , ist das Highlight unserer Dienstleistung.</p>
      <p>Ob fest integriert im Messestand, als mobi- le Espressobar mit eigener Theke oder als Coffeebike- wir haben für jeden Anlass die passende Variante.</p>
      <p>Branden Sie unser Equipment mit Ihrem Firmenlogo! Gerne beraten wir Sie hierzu.</p>
    </div>
  </section>

  <div class="photo" style="height:251px;background:linear-gradient(90deg,#8a7a6a,#c9b8a4 40%,#e6ddd3 60%,#a8998a)" role="img" aria-label="Hostess am Messestand im Gespräch mit einem Besucher"></div>

  <section class="block hostessen">
    <h2 class="heading">Hostessenagentur</h2>
    <div class="divider"></div>
    <p class="copy">Wählen Sie aus über 8.000 Hostessen und und mehr als 20 Sprachen!<br>Unsere Hostes- sen und Hosts begleiten Sie auf:</p>
    <ul class="services">
      <li>• Messen • Kongresse</li>
      <li>• VIP-Veranstaltungen • Promotion</li>
      <li>• Events aller Art</li>
    </ul>
    <a class="button" href="#">Jetzt informieren</a>
    <div class="cup" role="img" aria-label="Espressotasse mit Kaffeebohnen"></div>
  </section>

  <section class="cocktails">
    <h2 class="heading">Cocktails &amp; Smoothies<br>mit Firmenlogo</h2>
    <div class="divider"></div>
    <p class="copy">Unser mobiler Cocktailservice eignet sich für jede Art von<br>Veranstaltung und ist eine geniale Ergänzung zu jedem Messestand.<br>Erweitern Sie das bestehende Cocktailan- gebot mit gebrandeten<br>Smoothies in fünf verschiedenen Geschmacksrichtungen.</p>
    <a class="button" href="#">Jetzt informieren</a>
    <div class="leaf leaf-left" role="img" aria-label="Minzblätter"></div>
  </section>

  <section class="block messe">
    <h2 class="heading">Messecatering</h2>
    <div class="divider"></div>
    <p class="copy">Egal ob klassische Häppchen, trendiges Finger- food oder Menüs in<br>allen Variationen - sprechen Sie uns an!</p>
    <a class="button" href="#">Jetzt informieren</a>
  </section>

  <div class="photo" style="height:382px;background:radial-gradient(ellipse at 50% 60%,#c98a5a,#a5523e 40%,#e9e4de 85%)" role="img" aria-label="Häppchen mit Schinken, Frischkäse und Dill"></div>

  <section class="block news-head">
    <h2 class="heading">Aktuelles &amp; News</h2>
    <div class="divider"></div>
  </section>

  <div class="news-grid">
    <article class="card tint">
      <div class="card-photo" style="background:linear-gradient(180deg,#d6a46a,#3a3f52 45%,#e8e8ea)" role="img" aria-label="Barista an der Espressobar auf einer Messe"></div>
      <div class="card-body">
        <h3 class="card-title">Lorem Ipsum</h3><div class="divider"></div>
        <p class="card-copy">Lorem ipsum dolor sit amet, consec- tetuer adipiscing elit. Aenean commodo ligula eget dolor. Aenean massa...</p>
        <a class="button" href="#">Jetzt informieren</a>
      </div>
    </article>
    <article class="card">
      <div class="card-photo" style="background:linear-gradient(90deg,#9c8c7c,#d8cabd 50%,#ece6e0)" role="img" aria-label="Hostess am Messestand"></div>
      <div class="card-body">
        <h3 class="card-title">Lorem Ipsum</h3><div class="divider"></div>
        <p class="card-copy">Cum sociis natoque penatibus et magnis dis parturient montes, nascetur ridiculus mus pretium quis...</p>
        <a class="button" href="#">Jetzt informieren</a>
      </div>
    </article>
    <article class="card">
      <div class="card-photo" style="background:radial-gradient(ellipse at 50% 40%,#c89868,#f2eeea 50%,#b04a3a 95%)" role="img" aria-label="Cappuccino mit Latte Art"></div>
      <div class="card-body">
        <h3 class="card-title">Lorem Ipsum</h3><div class="divider"></div>
        <p class="card-copy">Cum sociis natoque penatibus et magnis dis parturient montes, nascetur ridiculus mus pretium quis...</p>
        <a class="button" href="#">Jetzt informieren</a>
      </div>
    </article>
    <article class="card tint">
      <div class="card-photo" style="background:linear-gradient(180deg,#d6a46a,#3a3f52 45%,#e8e8ea)" role="img" aria-label="Barista bereitet Kaffee am Messestand zu"></div>
      <div class="card-body">
        <h3 class="card-title">Lorem Ipsum</h3><div class="divider"></div>
        <p class="card-copy">Lorem ipsum dolor sit amet, consec- tetuer adipiscing elit. Aenean commodo ligula eget dolor. Aenean massa...</p>
        <a class="button" href="#">Jetzt informieren</a>
      </div>
    </article>
  </div>

  <footer class="footer">
    <div class="footer-brand">
      <span class="footer-rule"></span>
      <span class="brand-dot"></span><span class="brand-name">FALKENHOF KONTOR</span>
      <span class="footer-rule"></span>
    </div>
    <div class="addresses">
      <address style="font-style:normal"><strong>Standort Berlin</strong>Lindenhofweg 8<br>10997 Berlin<br>Tel. 030/ 41 27 58 30<br>Fax. 030/ 41 27 58 39<br>Mobil: 0151/ 246 81 35</address>
      <address style="font-style:normal"><strong>Standort Frankfurt</strong>Mainufergasse 21<br>60311 Frankfurt am Main<br>Tel. 069/ 87 620 114</address>
      <address style="font-style:normal"><strong>Standort München</strong>Kastanienallee 4<br>80999 München<br>Tel. 089/ 63 19 52 40<br>Fax. 089/ 63 19 52 49<br>Mobil: 0151/ 246 81 35</address>
    </div>
    <p class="unsubscribe">Falls Sie keinen Newsletter mehr wünschen,<br>können Sie ihn <a href="#">hier</a> abbestellen.</p>
    <div class="footer-line"></div>
    <div class="footer-bottom">
      <span><strong>Copyright © 2016 Falkenhof Kontor</strong> &nbsp;|&nbsp; Impressum</span>
      <div class="social"><span></span><span></span><span></span></div>
    </div>
  </footer>
</main>
<div class="leaf leaf-bottom" role="img" aria-label="Minzblätter"></div>
</body>
</html>
```